Information poster for parquet showroom

We are a parquet shop from germany and need some information poster for our showroom, to show our costumers some important information about parqut directly. The three posters are about reasons for parquet, and there are two types of paper on the subject. We would like to place the posters in a wooden frame. The design should be modern but simple. Enclosed I send you some of my ideas but it does not have to be like this. Can be completely different. I also send you some pictures of our showroom. 1st poster: Why parquet (dimension: 90x130 cm) Why parquet? - brings nature into your home - ecologically sustainable raw material - pleasantly warm - timeless% 26amp; high quality optics - durable% 26amp; reparable flooring - improved indoor climate - unique ride 2. Advantages oiled - tangible wood structure - natural appearance - scratches less present - partial repair possible advantage varnished - very easy-care - classic% 26amp; elegant appearance - protection against dirt and moisture - variable gloss level 3. Poster: overview of the hardness of different kinds of wood (dimension: 67x130 cm) wood hardness according to Brinell in N / mm² maple europ. 28 maple canadian. 35 birch 27 beech 33 oak 34 alder 17 ash 37 doussie 42 spruce 12 kambala 30 chestnut 18 pine 20 cherry european. 31 Larch 19 Merbau 44 Robinia 48 Sucupira 57 Elm 30 Wenge 45

```html
<!DOCTYPE html>
<html lang="de">
<head>
<meta charset="utf-8">
<title>Vorteil geölt – Vorteil lackiert</title>
<link rel="stylesheet" href="https://fonts.googleapis.com/css2?family=Alfa+Slab+One&display=swap">
<style>
  :root {
    --backdrop: #d1d2d4;
    --paper: #ffffff;
    --ink: #2c2d2d;
    --oiled: #f8b02e;
    --varnished: #f3622b;
    --pale: #d1d2d4;
  }
  * { margin: 0; padding: 0; box-sizing: border-box; }
  html, body {
    width: 1200px; height: 1200px; overflow: hidden;
    background: var(--backdrop);
    font-family: "Alfa Slab One", "Rockwell", serif;
  }
  .poster {
    position: absolute; left: 20px; top: 197px;
    width: 1160px; height: 806px;
    background: var(--paper);
    padding: 32px;
  }
  .board {
    position: relative; width: 100%; height: 100%;
    display: grid;
    grid-template-columns: 1fr 1fr;
    grid-template-rows: 208px 1fr;
  }
  .heading {
    background: var(--ink);
    position: relative;
  }
  .heading__line {
    position: absolute; left: 59px;
    font-size: 75px; line-height: 1;
    letter-spacing: 1px;
  }
  .heading--varnished .heading__line { left: 62px; }
  .heading__line--top { top: 32px; }
  .heading__line--bottom { top: 128px; color: var(--pale); }
  .heading--oiled .heading__line--top { color: var(--oiled); }
  .heading--varnished .heading__line--top { color: var(--varnished); }

  .benefits { position: relative; list-style: none; color: var(--ink); }
  .benefits--oiled { background: var(--oiled); }
  .benefits--varnished { background: var(--varnished); }
  .benefit {
    position: absolute; left: 30px; right: 20px;
    font-size: 26px; line-height: 37px; letter-spacing: 1.2px;
    text-transform: uppercase;
  }
  .benefits--varnished .benefit { left: 33px; }
  .benefits--varnished .divider {
    position: absolute; left: 0; right: 0; top: 133px;
    height: 1px; background: rgba(0,0,0,0.06);
  }
</style>
</head>
<body>
  <article class="poster">
    <div class="board">
      <header class="heading heading--oiled">
        <h2 class="heading__line heading__line--top">VORTEIL</h2>
        <h3 class="heading__line heading__line--bottom">GEÖLT</h3>
      </header>
      <header class="heading heading--varnished">
        <h2 class="heading__line heading__line--top">VORTEIL</h2>
        <h3 class="heading__line heading__line--bottom">LACKIERT</h3>
      </header>

      <ul class="benefits benefits--oiled">
        <li class="benefit" style="top:49px">Fühlbare Holzstruktur</li>
        <li class="benefit" style="top:183px">Natürliches Aussehen</li>
        <li class="benefit" style="top:299px">Kratzer weniger<br>präsent</li>
        <li class="benefit" style="top:440px">Partielle Ausbesserung<br>möglich</li>
      </ul>
      <ul class="benefits benefits--varnished">
        <li class="benefit" style="top:49px">Sehr pflegeleicht</li>
        <li class="divider" aria-hidden="true"></li>
        <li class="benefit" style="top:168px">Klassische &amp; elegante<br>Optik</li>
        <li class="benefit" style="top:299px">Schutz gegen Schmutz<br>&amp; Feuchtigkeit</li>
        <li class="benefit" style="top:463px">Variierbarer Glanzgrad</li>
      </ul>
    </div>
  </article>
</body>
</html>
```